New Frozen Vegetable Packaging for Retail

Hi all and welcome to our project! Looking for a versatile, enticing graphic design for our new frozen vegetable range packed in 250g bags sold at our grocery store.

We are a business located in Papua New Guinea and we manufacture and produce goods and have retail stores and restaurants. Our brand name for this product is ‘Yumba Fine’.

Target Audience: Our customers respond well to visual images rather than reading information, so keep it simple, bold and attractive! Our focus is - value for money.

Requirements:

• 1 x design so that we can easily change the description to fit multiple different products e.g. Mixed Vegetables / Frozen Peas / Frozen Corn
• Descriptions
o Mixed Vegetables (Product)
o Kwikim Friz to Preserve Freshness
o No Preservatives
o No Added Sugar
o No Artificial Colours or Flavours
o 250g NET

• Must have a clear window area for customers to see into the bag and visualise the product – would like around 20% of the bag to be clear.
• Our Yumba Fine Logo.
• An area for a barcode.
• Front and Back design.
• Require to be fully editable in either AI/PSD format.

No die line – please create the graphic for L20cm x W15cm with 1cm bleed (we will amend it to suit the products).

Thank you and look forward to collaborating on some great designs here :)

Target Market(s)

Budget, local Papua New Guinea customers

Industry/Entity Type

Retail Grocery

Font styles to use
Sans Serif

Requirements
Must have
• Generalised design to be adaptable to different products, logo, description, visual aids, window to see the product, barcode

```html
<!DOCTYPE html>
<html lang="en">
<head>
<meta charset="utf-8">
<title>Yumba Fine Mixed Vegetables – 250g Pack Front</title>
<link rel="stylesheet" href="https://fonts.googleapis.com/css2?family=Courgette&family=Outfit:wght@400;500;700;800&display=swap">
<style>
  :root {
    --backdrop: #e3e4e6;
    --pack-white: #f7f7f8;
    --seal-grey: #d9dadc;
    --orange: #e8711c;
    --orange-deep: #d0600f;
    --green-leaf: #2f9a24;
    --green-fresh: #7cc242;
    --green-light: #94cf4f;
    --brand-red: #b3141c;
    --ink: #1f2a14;
    --white: #ffffff;
  }
  * { margin: 0; padding: 0; box-sizing: border-box; }
  html, body { width: 1200px; height: 1200px; overflow: hidden; }
  body { background: var(--backdrop); position: relative; font-family: "Outfit", sans-serif; }

  .pack { position: absolute; left: 160px; top: 200px; width: 880px; height: 860px; }
  .pack-art { position: absolute; inset: 0; width: 880px; height: 860px; display: block; }

  .brand-name {
    position: absolute; left: 104px; top: 134px;
    font-family: "Outfit", sans-serif; font-weight: 800; font-size: 40px; line-height: 50px;
    color: var(--brand-red); display: flex; align-items: center; gap: 12px; white-space: nowrap;
  }
  .brand-name .brand-dot { width: 18px; height: 18px; border-radius: 50%; background: var(--brand-red); }

  .product-title {
    position: absolute; left: 370px; top: 152px; width: 400px;
    font-family: "Courgette", cursive; font-weight: 400; color: var(--white);
    font-size: 80px; line-height: 80px; text-align: center;
    text-shadow:
      3px 0 0 var(--orange-deep), -3px 0 0 var(--orange-deep),
      0 3px 0 var(--orange-deep), 0 -3px 0 var(--orange-deep),
      2px 2px 0 var(--orange-deep), -2px -2px 0 var(--orange-deep),
      2px -2px 0 var(--orange-deep), -2px 2px 0 var(--orange-deep);
  }
  .product-title span { display: block; white-space: nowrap; }
  .product-title .line-one { margin-left: 20px; }

  .tagline {
    position: absolute; left: 116px; top: 764px;
    font-size: 23px; font-weight: 400; color: var(--ink); white-space: nowrap;
  }
  .net-weight {
    position: absolute; left: 630px; top: 760px;
    font-size: 28px; font-weight: 700; color: var(--ink); white-space: nowrap;
  }
</style>
</head>
<body>
  <div class="pack">
    <svg class="pack-art" viewBox="340 330 1350 1320" preserveAspectRatio="none" xmlns="http://www.w3.org/2000/svg">
      <defs>
        <linearGradient id="window-fill" x1="0" y1="0" x2="1" y2="1">
          <stop offset="0" stop-color="#f0a070"/>
          <stop offset="0.35" stop-color="#b9d98a"/>
          <stop offset="0.6" stop-color="#f2b27e"/>
          <stop offset="1" stop-color="#a9d07a"/>
        </linearGradient>
        <linearGradient id="green-fill" x1="0" y1="0" x2="0" y2="1">
          <stop offset="0" stop-color="#7cc242"/>
          <stop offset="1" stop-color="#94cf4f"/>
        </linearGradient>
        <linearGradient id="orange-fill" x1="0" y1="0" x2="1" y2="0">
          <stop offset="0" stop-color="#cf5a0c"/>
          <stop offset="0.6" stop-color="#e8711c"/>
          <stop offset="1" stop-color="#f08a35"/>
        </linearGradient>
        <path id="arc-top-1" d="M1057,1385 a48,48 0 0 1 96,0"/>
        <path id="arc-bot-1" d="M1047,1385 a58,58 0 0 0 116,0"/>
        <path id="arc-top-2" d="M1222,1385 a48,48 0 0 1 96,0"/>
        <path id="arc-bot-2" d="M1212,1385 a58,58 0 0 0 116,0"/>
        <path id="arc-top-3" d="M1392,1385 a48,48 0 0 1 96,0"/>
        <path id="arc-bot-3" d="M1382,1385 a58,58 0 0 0 116,0"/>
      </defs>

      <rect class="pack-body" x="345" y="335" width="1345" height="1315" rx="12" fill="var(--pack-white)"/>
      <rect class="seal-top" x="345" y="335" width="1345" height="55" rx="10" fill="var(--seal-grey)"/>

      <rect class="orange-band" x="1000" y="360" width="360" height="740" fill="url(#orange-fill)"/>

      <path class="green-base" fill="url(#green-fill)"
        d="M345,1455 L430,1450 C1000,1400 1220,1100 1270,890 C1255,960 1245,1030 1230,1090 L1690,1090 L1690,1650 L345,1650 Z"/>
      <rect class="green-stripe" x="1230" y="1090" width="460" height="60" fill="var(--green-leaf)" opacity="0.8"/>

      <path class="product-window" role="img" aria-label="Clear window showing frozen carrots, peas, corn and green beans"
        d="M430,935 C700,900 1050,1000 1270,890 C1220,1100 1000,1400 430,1450 Z"
        fill="url(#window-fill)" stroke="var(--green-leaf)" stroke-width="10" stroke-linejoin="round"/>

      <rect class="seal-bottom" x="345" y="1595" width="1345" height="55" rx="10" fill="var(--green-leaf)" opacity="0.55"/>

      <g class="claim-badges" fill="none" stroke="var(--white)" stroke-width="4">
        <circle cx="1105" cy="1385" r="64"/>
        <circle cx="1105" cy="1385" r="36"/>
        <line x1="1088" y1="1402" x2="1122" y2="1368"/>
        <circle cx="1270" cy="1385" r="64"/>
        <circle cx="1270" cy="1385" r="36"/>
        <path d="M1263,1368 v12 l-12,20 h38 l-12,-20 v-12"/>
        <circle cx="1440" cy="1385" r="64"/>
        <circle cx="1440" cy="1385" r="36"/>
        <rect x="1428" y="1373" width="24" height="24"/>
      </g>
      <g class="claim-badge-text" fill="var(--white)" font-family="Outfit, sans-serif" font-weight="700" font-size="12" letter-spacing="0.5">
        <text><textPath href="#arc-top-1" startOffset="50%" text-anchor="middle">NO ARTIFICIAL</textPath></text>
        <text><textPath href="#arc-bot-1" startOffset="50%" text-anchor="middle">COLOURS OR FLAVOURS</textPath></text>
        <text><textPath href="#arc-top-2" startOffset="50%" text-anchor="middle">NO PRESERVATIVES</textPath></text>
        <text><textPath href="#arc-bot-2" startOffset="50%" text-anchor="middle">NO PRESERVATIVES</textPath></text>
        <text><textPath href="#arc-top-3" startOffset="50%" text-anchor="middle">NO ADDED SUGAR</textPath></text>
        <text><textPath href="#arc-bot-3" startOffset="50%" text-anchor="middle">NO ADDED SUGAR</textPath></text>
      </g>
    </svg>

    <div class="brand-name"><span class="brand-dot"></span>Yumba Fine</div>

    <h1 class="product-title"><span class="line-one">Mixed</span><span class="line-two">Vegetables</span></h1>

    <p class="tagline">Kwikim Friz to Preserve Freshness</p>
    <p class="net-weight">250g NET</p>
  </div>
</body>
</html>
```